Business card: floral shop

I own a flower shop that specializes in Japanese flower settings and weddings. I am looking for a design that has to be colorful, but elegantly simple (unadorned), while implying class, love, and commitment.

My flower shop is also all about outstanding customer service, if this helps at all.

Industry/Entity Type

Floral

Contact Information for Business Card

Company Name: Brightwater Bloom Studio
Name: Marisol Keene
Address: 41 Larkspur Rd, Wexley, MA 01836
Email: petalcrestmail@fernovo.com

Logo Text

Brightwater Bloom Studio

Requirements
Must have
• Flowers, color, company information.

Offer:

"Refer a friend and receive $25 gift certificate at the time of the order"
Should not have
• Black borders

```html
<!DOCTYPE html>
<html lang="en">
<head>
<meta charset="utf-8">
<title>Brightwater Bloom Studio – Business Card</title>
<link rel="stylesheet" href="https://fonts.googleapis.com/css2?family=Dancing+Script:wght@500&family=Kalam:wght@400&family=Tinos&family=Arimo:wght@700&display=swap">
<style>
  :root {
    --paper: #f4f4f4;
    --petal-light: #ffffff;
    --petal-mid: #e2e2e2;
    --petal-shade: #b9b9b9;
    --brand-navy: #1f3a6b;
    --ink-charcoal: #333333;
    --ink-maroon: #8b1a1a;
    --ink-amber: #a0621a;
    --offer-indigo: #2a1a5a;
    --offer-mauve: #b79cbc;
    --offer-shadow: rgba(60, 60, 60, 0.55);
    --contact-plum: #4a0a4a;
  }
  html, body {
    margin: 0;
    padding: 0;
    overflow: hidden;
    background: var(--paper);
  }
  .card {
    position: relative;
    width: 1200px;
    height: 741px;
    overflow: hidden;
    background: var(--paper);
  }
  .flower-backdrop {
    position: absolute;
    inset: 0;
    background:
      radial-gradient(ellipse 38% 42% at 42% 40%, var(--petal-light) 0%, var(--petal-mid) 55%, transparent 80%),
      radial-gradient(ellipse 45% 60% at 80% 45%, var(--petal-light) 0%, var(--petal-mid) 60%, transparent 85%),
      radial-gradient(ellipse 60% 40% at 30% 75%, var(--petal-light) 0%, transparent 70%),
      linear-gradient(120deg, var(--petal-mid) 0%, var(--petal-light) 40%, var(--petal-shade) 100%);
  }
  .card > p, .card > h1 {
    position: absolute;
    margin: 0;
    white-space: nowrap;
    line-height: 1;
  }
  .brand-name {
    top: 62px;
    left: 0;
    width: 1200px;
    text-align: center;
    font-family: "Dancing Script", cursive;
    font-weight: 500;
    font-size: 46px;
    color: var(--brand-navy);
  }
  .tagline-lead {
    top: 158px;
    left: 416px;
    font-family: "Kalam", cursive;
    font-size: 36px;
    color: var(--ink-charcoal);
  }
  .tagline-joiner {
    top: 206px;
    left: 503px;
    font-family: "Kalam", cursive;
    font-size: 34px;
    color: var(--ink-maroon);
  }
  .tagline-specialty {
    top: 256px;
    left: 144px;
    font-family: "Kalam", cursive;
    font-size: 37px;
    color: var(--ink-amber);
  }
  .offer-label {
    top: 338px;
    left: 22px;
    font-family: "Tinos", serif;
    font-size: 28px;
    color: var(--offer-indigo);
  }
  .offer-text {
    top: 386px;
    left: 51px;
    font-family: "Dancing Script", cursive;
    font-weight: 500;
    font-size: 33px;
    color: var(--offer-mauve);
    -webkit-text-stroke: 0.6px var(--contact-plum);
    text-shadow: 2px 4px 5px var(--offer-shadow);
  }
  .contact {
    left: 24px;
    font-family: "Arimo", sans-serif;
    font-weight: 700;
    font-size: 34px;
    color: var(--contact-plum);
  }
  .contact-name { top: 545px; }
  .contact-address { top: 591px; }
  .contact-email { top: 633px; }
</style>
</head>
<body>
  <main class="card">
    <div class="flower-backdrop" role="img" aria-label="Soft black-and-white close-up photograph of a large white ranunculus bloom filling the card"></div>

    <h1 class="brand-name">Brightwater Bloom Studio</h1>

    <p class="tagline-lead">Specializes</p>
    <p class="tagline-joiner">in</p>
    <p class="tagline-specialty">Japanese Flower Settings and Weddings</p>

    <p class="offer-label">Offer-:</p>
    <p class="offer-text">"Refer a friend and receive $25 gift certificate at the time of the order"</p>

    <p class="contact contact-name">Marisol Keene</p>
    <p class="contact contact-address">41 Larkspur Rd, Wexley, MA 01836</p>
    <p class="contact contact-email">petalcrestmail@fernovo.com</p>
  </main>
</body>
</html>
```